Zentro - revolutionary mobile payment

The app is a P2P money trasfert, without the using of credit card or bank circuits it can transfer electronic money from one person to another consumers simply and immediatelly.
You can use the color you want, but the message we need to transert to consumer is simplicity, safety and coolness.
In attach the logo of the company and the wireframe of thre page of the app.
The goal is to design the page of the app with a clear, simple and intuitive graphic.
Updates

I have upgrade the brief with important information and detail, many thanks

Target Market(s)

all the people

Industry/Entity Type

Credit Card

Requirements
Must have
• You have to design one icon for each button in the first page, (shop is: where to shop)
in the second one a new intuitive image (instead of the hand) that let the user to understand that with a simple swipe he can process the payment
Nice to have
• You can include or esxclude what you want or belive can improve user experience of the app
Should not have
• too much color, too much button or information

```html
<!DOCTYPE html>
<html lang="en">
<head>
<meta charset="utf-8">
<title>Zentro — mobile payment app screens</title>
<link href="https://fonts.googleapis.com/css2?family=Jost:wght@400;500;600;700&display=swap" rel="stylesheet">
<style>
  :root{
    --navy:#1c3362;
    --navy-dark:#162a52;
    --navy-soft:#4b5f8c;
    --sky:#dfe9f8;
    --sky-deep:#cfdcf1;
    --paper:#ffffff;
    --mist:#ececec;
    --field:#ebebeb;
    --ink:#2a3550;
    --muted:#9aa0ab;
    --label-red:#ff1a1a;
    --stage:#000000;
    --keys-bg:#d2d5db;
  }
  *{box-sizing:border-box;margin:0;padding:0}
  html,body{width:1200px;height:1000px;overflow:hidden;background:var(--stage)}
  body{position:relative;font-family:"Jost",sans-serif;color:var(--ink)}
  .screen{position:absolute;overflow:hidden;background:var(--paper)}
  .option-label{position:absolute;color:var(--label-red);font-family:"Jost",sans-serif;font-size:40px;font-weight:400;line-height:1}
  .wordmark{font-family:"Jost",sans-serif;font-weight:700;color:var(--paper);letter-spacing:.5px;display:flex;align-items:center;gap:5px}
  .wordmark .dot{width:12px;height:12px;border-radius:50%;border:2px solid currentColor}
  .avatar{position:absolute;border-radius:50%;background:radial-gradient(circle at 50% 40%,#f4f4f4,#d6d6d6)}
  .status-bar{position:absolute;left:0;right:0;top:0;height:18px;background:var(--navy);color:var(--paper);font-size:9px;display:flex;align-items:center;justify-content:space-between;padding:0 6px}
  .status-bar .battery{display:inline-block;width:18px;height:8px;border:1px solid var(--paper);margin-left:3px;vertical-align:middle;position:relative}
  .status-bar .battery::after{content:"";position:absolute;left:1px;top:1px;width:4px;height:4px;background:var(--paper)}
  .hamburger{position:absolute;width:18px;height:11px;border-top:2px solid var(--paper);border-bottom:2px solid var(--paper)}
  .hamburger::after{content:"";position:absolute;left:0;right:0;top:3.5px;height:2px;background:var(--paper)}
  .action{position:absolute;display:flex;flex-direction:column;align-items:center;width:100px}
  .action svg{width:74px;height:74px}
  .action span{font-size:12px;font-weight:500;color:var(--ink);margin-top:6px}

  /* login */
  .login{left:34px;top:31px;width:252px;height:447px;background:linear-gradient(180deg,#e9e7f3 0%,#f3f3f3 40%,#dcdcdc 100%)}
  .login .brand{position:absolute;left:0;right:0;top:100px;display:flex;justify-content:center}
  .login .brand .wordmark{color:var(--navy);font-size:26px}
  .login .brand .dot{width:18px;height:18px;border-width:3px}
  .input{position:absolute;left:28px;width:196px;height:30px;border-radius:15px;background:var(--paper);display:flex;align-items:center;padding-left:12px;font-size:11px;color:#777;gap:9px}
  .btn{position:absolute;border-radius:16px;background:var(--navy);color:var(--paper);font-weight:600;display:flex;align-items:center;justify-content:center}
  .login .footer{position:absolute;left:35px;right:22px;bottom:9px;display:flex;justify-content:space-between;font-size:8px;color:#555}

  /* option 1 */
  .opt1{left:328px;top:30px;width:252px;height:448px;background:var(--sky)}
  .opt1 .head{position:absolute;left:0;top:0;width:252px;height:195px;background:var(--navy)}
  .opt1 .head::after{content:"";position:absolute;left:50%;bottom:-8px;margin-left:-8px;border:8px solid transparent;border-bottom:0;border-top-color:var(--navy)}
  .name{position:absolute;left:0;right:0;text-align:center;color:var(--paper);font-weight:600}
  .sub{position:absolute;left:0;right:0;text-align:center;color:#c6d0e4;font-size:10px}
  .cell{position:absolute;width:126px;height:126px;border:1px solid #edf2fb}
  .cell.active{background:var(--sky-deep)}

  /* option 2 */
  .opt2{left:624px;top:30px;width:252px;height:448px;background:linear-gradient(180deg,#ececec 0%,#e4e4e4 60%,#f2f2f2 100%)}
  .navbar{position:absolute;left:0;right:0;top:18px;height:32px;background:var(--navy)}

  /* menu */
  .menu{left:919px;top:30px;width:252px;height:448px;background:var(--paper)}
  .menu .drawer{position:absolute;left:0;top:0;width:201px;height:448px;background:var(--navy)}
  .menu .peek{position:absolute;left:201px;top:0;width:51px;height:448px;background:#ededed}
  .menu .peek .strip{position:absolute;left:0;right:0;top:0;height:50px;background:var(--navy)}
  .menu-item{position:absolute;left:0;width:201px;height:38px;display:flex;align-items:center;gap:8px;padding-left:15px;color:var(--paper);font-size:11px}
  .menu-item.active{background:var(--navy-dark)}

  /* balance */
  .balance{left:624px;top:519px;width:261px;height:464px;background:var(--paper)}
  .balance .head{position:absolute;left:0;top:0;width:261px;height:201px;background:var(--navy)}
  .back{position:absolute;width:20px;height:20px;border-radius:50%;border:1.5px solid var(--paper)}
  .back::after{content:"";position:absolute;left:7px;top:5px;width:5px;height:5px;border-left:1.5px solid var(--paper);border-bottom:1.5px solid var(--paper);transform:rotate(45deg)}
  .filter-band{position:absolute;left:0;top:201px;width:261px;height:58px;background:var(--sky)}
  .select{position:absolute;left:13px;top:12px;width:235px;height:32px;border-radius:16px;background:var(--paper);font-size:11px;color:var(--muted);display:flex;align-items:center;padding-left:12px}
  .select .chev{position:absolute;right:8px;top:8px;width:16px;height:16px;border-radius:50%;background:var(--navy)}
  .select .chev::after{content:"";position:absolute;left:5px;top:4px;width:5px;height:5px;border-right:1.5px solid #fff;border-bottom:1.5px solid #fff;transform:rotate(45deg)}
  .tx{position:absolute;left:13px;width:235px;height:32px;border-radius:16px;background:var(--field);display:flex;align-items:center;padding-left:12px;font-size:11px;color:#b6b6b6}
  .tx .amt{position:absolute;left:147px;color:#555}
  .tx .go{position:absolute;right:7px;top:8px;width:16px;height:16px;border-radius:50%;background:#d3d3d3}
  .tx .go::after{content:"";position:absolute;left:4px;top:5px;width:5px;height:5px;border-right:1.5px solid #fff;border-top:1.5px solid #fff;transform:rotate(45deg)}

  /* pay */
  .pay{left:910px;top:519px;width:261px;height:464px;background:var(--paper)}
  .pay .navbar{height:30px}
  .pay .title{position:absolute;left:0;right:0;top:20px;text-align:center;color:var(--paper);font-weight:700;font-size:13px;letter-spacing:1px}
  .pay .phone-band{position:absolute;left:0;top:48px;width:261px;height:55px;background:var(--sky)}
  .pill{position:absolute;height:30px;border-radius:15px;background:var(--paper);display:flex;align-items:center;font-size:12px;color:#999}
  .keyboard{position:absolute;left:0;top:287px;width:261px;height:177px;background:var(--keys-bg);padding:8px 3px 0}
  .krow{display:flex;justify-content:center;gap:4px;margin-bottom:9px}
  .key{height:30px;width:21px;background:var(--paper);border-radius:4px;font-size:15px;display:flex;align-items:center;justify-content:center;color:#222;box-shadow:0 1px 0 #8e9096}
  .key.fn{background:#b3b7bf;font-size:11px}

  /* app icons */
  .app-icon{position:absolute;width:217px;height:217px;border-radius:44px;display:flex;align-items:center;justify-content:center}
  .app-icon.light{left:34px;top:541px;background:linear-gradient(180deg,#ffffff,#e1e1e1);border:1px solid #bbb}
  .app-icon.dark{left:252px;top:740px;background:var(--navy)}
  .app-icon .wordmark{font-size:34px;gap:8px}
  .app-icon .dot{width:22px;height:22px;border-width:4px}
</style>
</head>
<body>

<svg width="0" height="0" style="position:absolute" aria-hidden="true">
  <defs>
    <symbol id="ring" viewBox="0 0 80 80">
      <circle cx="40" cy="40" r="40" fill="currentColor"/>
      <path d="M20 50 A22 22 0 0 1 50 20" stroke="#fff" stroke-width="3" fill="none" stroke-linecap="round"/>
      <path d="M60 30 A22 22 0 0 1 30 60" stroke="#fff" stroke-width="3" fill="none" stroke-linecap="round"/>
      <path d="M46 15 L52 20 L45 24" stroke="#fff" stroke-width="3" fill="none" stroke-linecap="round"/>
      <path d="M34 65 L28 60 L35 56" stroke="#fff" stroke-width="3" fill="none" stroke-linecap="round"/>
    </symbol>
    <symbol id="i-pay" viewBox="0 0 80 80">
      <use href="#ring"/>
      <rect x="29" y="34" width="22" height="14" rx="2" fill="none" stroke="#fff" stroke-width="2.2"/>
      <line x1="29" y1="39" x2="51" y2="39" stroke="#fff" stroke-width="2.2"/>
      <path d="M40 34 L50 26 L54 30" stroke="#fff" stroke-width="2.2" fill="none"/>
    </symbol>
    <symbol id="i-ask" viewBox="0 0 80 80">
      <use href="#ring"/>
      <text x="40" y="49" text-anchor="middle" font-family="Jost, sans-serif" font-weight="700" font-size="26" fill="#fff">?</text>
    </symbol>
    <symbol id="i-account" viewBox="0 0 80 80">
      <use href="#ring"/>
      <path d="M28 34 L40 27 L52 34 Z" fill="#fff"/>
      <rect x="31" y="36" width="3" height="10" fill="#fff"/>
      <rect x="38.5" y="36" width="3" height="10" fill="#fff"/>
      <rect x="46" y="36" width="3" height="10" fill="#fff"/>
      <rect x="28" y="47" width="24" height="3" fill="#fff"/>
    </symbol>
    <symbol id="i-shop" viewBox="0 0 80 80">
      <use href="#ring"/>
      <path d="M27 31 H31 L35 45 H50 L53 35 H33" stroke="#fff" stroke-width="2.2" fill="none" stroke-linejoin="round"/>
      <circle cx="37" cy="49" r="2" fill="#fff"/>
      <circle cx="48" cy="49" r="2" fill="#fff"/>
    </symbol>
  </defs>
</svg>

<!-- Login -->
<section class="screen login">
  <div class="brand"><span class="wordmark"><span class="dot"></span>Zentro</span></div>
  <div class="input" style="top:201px">
    <svg width="12" height="12" viewBox="0 0 12 12"><circle cx="6" cy="4" r="2.6" fill="none" stroke="#555"/><path d="M1 11.5 C1 7.5 11 7.5 11 11.5" fill="none" stroke="#555"/></svg>E-mail address
  </div>
  <div class="input" style="top:240px">
    <svg width="12" height="12" viewBox="0 0 12 12"><rect x="1.5" y="5" width="9" height="6.5" fill="none" stroke="#555"/><path d="M3.5 5 V3.5 a2.5 2.5 0 0 1 5 0" fill="none" stroke="#555"/></svg><span style="color:#333;letter-spacing:2px">••••••••</span>
    <svg style="position:absolute;right:10px" width="14" height="9" viewBox="0 0 14 9"><ellipse cx="7" cy="4.5" rx="6.5" ry="4" fill="#ccc"/><circle cx="7" cy="4.5" r="2" fill="#fff"/></svg>
  </div>
  <div class="btn" style="left:28px;top:285px;width:196px;height:31px;font-size:12px">Sign in</div>
  <div class="footer"><span>Forgot password?</span><span>New here? Sign Up</span></div>
</section>

<!-- Option 1 -->
<section class="screen opt1">
  <div class="head">
    <svg style="position:absolute;left:11px;top:10px" width="20" height="20" viewBox="0 0 20 20"><circle cx="10" cy="10" r="9" fill="none" stroke="#fff" stroke-width="1.4"/><path d="M6 7H14M6 10H14M6 13H14" stroke="#fff" stroke-width="1.4"/></svg>
    <div style="position:absolute;left:0;right:0;top:12px;display:flex;justify-content:center"><span class="wordmark" style="font-size:14px"><span class="dot"></span>Zentro</span></div>
    <div class="avatar" role="img" aria-label="Profile picture placeholder" style="left:89px;top:67px;width:74px;height:74px"></div>
    <div class="name" style="top:137px;font-size:11px">Marco Delling</div>
    <div class="sub" style="top:153px">+3020000147</div>
  </div>
  <div class="cell active" style="left:0;top:195px"></div>
  <div class="cell" style="left:126px;top:195px"></div>
  <div class="cell" style="left:0;top:321px"></div>
  <div class="cell" style="left:126px;top:321px"></div>
  <div class="action" style="left:13px;top:218px;color:var(--navy)"><svg><use href="#i-pay"/></svg><span>Pay</span></div>
  <div class="action" style="left:141px;top:218px;color:var(--navy)"><svg><use href="#i-ask"/></svg><span>Ask</span></div>
  <div class="action" style="left:13px;top:343px;color:var(--navy)"><svg><use href="#i-account"/></svg><span>Account</span></div>
  <div class="action" style="left:141px;top:343px;color:var(--navy)"><svg><use href="#i-shop"/></svg><span>Shop</span></div>
</section>
<div class="option-label" style="left:338px;top:495px">option_1</div>

<!-- Option 2 -->
<section class="screen opt2">
  <div class="status-bar"><span>●●●○○ NOVA</span><span>4:21 PM</span><span>22%<i class="battery"></i></span></div>
  <div class="navbar">
    <span class="hamburger" style="left:6px;top:11px"></span>
    <div style="position:absolute;left:0;right:0;top:7px;display:flex;justify-content:center"><span class="wordmark" style="font-size:14px"><span class="dot"></span>Zentro</span></div>
    <svg style="position:absolute;right:6px;top:8px" width="16" height="16" viewBox="0 0 16 16"><circle cx="8" cy="8" r="5.5" fill="none" stroke="#fff" stroke-width="2" stroke-dasharray="2.5 1.8"/><circle cx="8" cy="8" r="2.2" fill="none" stroke="#fff" stroke-width="1.3"/></svg>
  </div>
  <div class="action" style="left:17px;top:95px;color:var(--navy)"><svg><use href="#i-pay"/></svg><span>Pay</span></div>
  <div class="action" style="left:134px;top:95px;color:var(--navy-soft)"><svg><use href="#i-ask"/></svg><span>Ask</span></div>
  <div class="action" style="left:17px;top:214px;color:var(--navy-soft)"><svg><use href="#i-account"/></svg><span>Account</span></div>
  <div class="action" style="left:134px;top:214px;color:var(--navy-soft)"><svg><use href="#i-shop"/></svg><span>Shop</span></div>
  <div role="img" aria-label="Faint world map backdrop" style="position:absolute;left:0;right:0;bottom:0;height:120px;background:linear-gradient(180deg,rgba(255,255,255,0),rgba(255,255,255,.55))"></div>
</section>
<div class="option-label" style="left:661px;top:443px">option_2</div>

<!-- Side menu -->
<section class="screen menu">
  <div class="peek">
    <div class="strip"></div>
    <div style="position:absolute;left:0;top:0;right:0;height:18px;color:#fff;font-size:9px;padding:5px 0 0 4px">●●●○ NOVA</div>
    <span class="hamburger" style="left:6px;top:29px"></span>
    <div style="position:absolute;left:33px;top:96px;width:74px;height:74px;border-radius:50%;background:var(--navy)"></div>
    <div style="position:absolute;left:33px;top:215px;width:74px;height:74px;border-radius:50%;background:var(--navy-soft)"></div>
  </div>
  <div class="drawer">
    <div style="position:absolute;left:60px;top:18px;width:84px;height:84px;border-radius:50%;background:#243d70"></div>
    <div class="avatar" role="img" aria-label="Profile picture placeholder" style="left:66px;top:24px;width:72px;height:72px"></div>
    <div class="name" style="top:113px;font-size:15px">Marco Delling</div>
    <div class="sub" style="top:134px;font-size:11px">+360000482716</div>
    <div class="menu-item" style="top:164px">
      <svg width="20" height="20" viewBox="0 0 20 20"><circle cx="10" cy="10" r="9" fill="none" stroke="#fff" stroke-width="1.2"/><circle cx="10" cy="8" r="3" fill="none" stroke="#fff" stroke-width="1.2"/><path d="M4.5 15.5 C6 11.5 14 11.5 15.5 15.5" fill="none" stroke="#fff" stroke-width="1.2"/></svg>Total Balance
    </div>
    <div class="menu-item active" style="top:203px">
      <svg width="20" height="20" viewBox="0 0 20 20"><circle cx="10" cy="10" r="7" fill="none" stroke="#fff" stroke-width="2.4" stroke-dasharray="3 2"/><circle cx="10" cy="10" r="3" fill="none" stroke="#fff" stroke-width="1.2"/></svg>Profile Settings
    </div>
    <div class="menu-item" style="top:403px">
      <svg width="18" height="16" viewBox="0 0 18 16"><path d="M8 1H1V15H8" fill="none" stroke="#fff" stroke-width="1.2"/><path d="M5 8H16M12 4L16 8L12 12" fill="none" stroke="#fff" stroke-width="1.2"/></svg>Log out
    </div>
  </div>
</section>

<!-- Balance -->
<section class="screen balance">
  <div class="head">
    <span class="back" style="left:11px;top:10px"></span>
    <div style="position:absolute;left:0;right:0;top:12px;display:flex;justify-content:center"><span class="wordmark" style="font-size:14px"><span class="dot"></span>Zentro</span></div>
    <div class="avatar" role="img" aria-label="Profile picture placeholder" style="left:92px;top:56px;width:77px;height:77px"></div>
    <div class="name" style="top:142px;font-size:11px">Your Balance</div>
    <div class="sub" style="top:159px">€240523.23</div>
  </div>
  <div class="filter-band"><div class="select">ultimi 30 giorni<span class="chev"></span></div></div>
  <div class="tx" style="top:280px">+3590001234567<span class="amt">€2</span><span class="go"></span></div>
  <div class="tx" style="top:336px">+3590001234567<span class="amt">€-2</span><span class="go"></span></div>
  <div class="btn" style="left:23px;top:409px;width:100px;height:32px;font-size:11px">Report</div>
  <div class="btn" style="left:139px;top:409px;width:100px;height:32px;font-size:11px">Tache</div>
</section>

<!-- Pay -->
<section class="screen pay">
  <div class="status-bar"><span>●●●○○ NOVA</span><span>4:21 PM</span><span>22%<i class="battery"></i></span></div>
  <div class="navbar"></div>
  <span class="back" style="left:12px;top:22px"></span>
  <div class="title">PAY</div>
  <div class="phone-band">
    <div class="pill" style="left:13px;top:12px;width:63px;justify-content:center">+39</div>
    <div class="pill" style="left:86px;top:12px;width:162px;padding-left:11px;color:#888">0123456789</div>
  </div>
  <div class="pill" style="left:13px;top:119px;width:235px;padding-left:12px;background:var(--field);color:#555"><b style="color:#333;margin-right:10px">€</b>0,000</div>
  <div class="keyboard">
    <div class="krow"><span class="key">Q</span><span class="key">W</span><span class="key">E</span><span class="key">R</span><span class="key">T</span><span class="key">Y</span><span class="key">U</span><span class="key">I</span><span class="key">O</span><span class="key">P</span></div>
    <div class="krow"><span class="key">A</span><span class="key">S</span><span class="key">D</span><span class="key">F</span><span class="key">G</span><span class="key">H</span><span class="key">J</span><span class="key">K</span><span class="key">L</span></div>
    <div class="krow"><span class="key fn" style="width:30px">⇧</span><span style="width:4px"></span><span class="key">Z</span><span class="key">X</span><span class="key">C</span><span class="key">V</span><span class="key">B</span><span class="key">N</span><span class="key">M</span><span style="width:4px"></span><span class="key fn" style="width:30px">⌫</span></div>
    <div class="krow"><span class="key fn" style="width:25px">123</span><span class="key fn" style="width:25px">◎</span><span class="key fn" style="width:25px">♪</span><span class="key" style="width:38px;font-size:11px">space</span><span class="key" style="width:25px;font-size:13px">@</span><span class="key" style="width:25px">.</span><span class="key fn" style="width:60px;font-size:12px">return</span></div>
  </div>
</section>

<!-- App icons -->
<div class="app-icon light"><span class="wordmark" style="color:var(--navy)"><span class="dot"></span>Zentro</span></div>
<div class="option-label" style="left:279px;top:603px">App icon_1</div>
<div class="app-icon dark"><span class="wordmark"><span class="dot"></span>Zentro</span></div>
<div class="option-label" style="left:32px;top:892px">App icon_2</div>

</body>
</html>
```